Orient Wager Digest Quarterly Magazine

We need a magazine design for a new company based in Asia called Orient Wager Digest (OWD).

OWD provide up to date market information for worldwide executives on relevant gaming issues in Asia, covering:
- specific market and legal challenges
- new regulations and their implications for the
industry
- company operations in different jurisdictions (country specific)
- governance and compliance issues
- financing, HR and technology trends

This magazine design must be high-end and relate more to a business periodical/journal that exhibits reliability and industry expertise than a fashion magazine. For reference purpose see Verdant Magazine and their previous issue. It is important that this design project has synergy with our previous two magazines (see file uploads).

You can also visit http://www.orientwagerdigest-example.com, however we are in the process of updating this website.

Initially, we would like to see a conceptual SCAMP for 3 spread layouts, including the following pages:

- Main country page template full-spread (text, image, snippet and data/diagram/graph)
- Editorial page
- Contents page
- Sponsors page
- Front Cover

Specific Requirements:
Page Width = 200mm
Page Height = 265mm
Trim measurement = we usually use 5mm
Corporate Colors = Red #990000, Green #226727
Gutter measurement for a 60 page mag, give or take
(*note that most of the odd pages will be Advertising pages consisting of a full page image, therefore they will not need much work.)
Images can bleed off page

Must Haves:
experience in magazine design
able to work with google drive
able to plot graphs, design diagrams, charts etc...

To All,

Logo version has just been uploaded.

Cheers

```html
<!DOCTYPE html>
<html lang="en">
<head>
<meta charset="UTF-8">
<title>Orient Wager Digest — Editor's Letter Spread</title>
<link href="https://fonts.googleapis.com/css2?family=Roboto:wght@100;300;400;700&family=Great+Vibes&display=swap" rel="stylesheet">
<style>
  :root {
    --brand-red: #981b1e;
    --paper: #ffffff;
    --backdrop: #e6e6e6;
    --ink: #2b2b2b;
    --ink-soft: #555555;
    --rule: #c9c9c9;
    --photo-warm: #6b4128;
    --photo-deep: #2d1a12;
  }
  * { box-sizing: border-box; margin: 0; padding: 0; }
  html, body {
    width: 1200px; height: 800px; overflow: hidden;
    background: var(--backdrop);
    font-family: "Roboto", Arial, sans-serif;
    color: var(--ink);
  }
  .spread {
    position: absolute; left: 72px; top: 50px;
    width: 1056px; height: 700px;
    display: flex;
    box-shadow: 0 6px 24px rgba(0,0,0,.18);
  }
  .page {
    position: relative; width: 528px; height: 700px;
    background: var(--paper); overflow: hidden;
  }
  .page--left { background: linear-gradient(to right, #fff 88%, #ececec 100%); }
  .page--right { background: linear-gradient(to left, #fff 88%, #ececec 100%); }

  .running-head {
    position: absolute; top: 18px; font-size: 10px; color: var(--ink-soft);
    letter-spacing: .3px;
  }
  .page--left .running-head { left: 26px; }
  .page--right .running-head { right: 34px; top: 34px; }
  .running-head-rule {
    position: absolute; top: 50px; right: 34px; width: 150px; height: 1px; background: var(--rule);
  }
  .side-title {
    position: absolute; font-size: 9px; letter-spacing: 1px; text-transform: uppercase;
    color: var(--ink-soft); white-space: nowrap;
  }
  .page--left .side-title {
    left: 20px; top: 60px; transform-origin: left top; transform: rotate(90deg) translateY(-10px);
  }
  .page--right .side-title {
    right: 8px; top: 60px; transform-origin: right top; transform: rotate(90deg) translateX(100%);
  }

  .editor-portrait {
    position: absolute; left: 82px; top: 80px; width: 148px; height: 168px;
    background: linear-gradient(160deg, #c98a86 0%, #8a5a4c 55%, #3d2a26 100%);
  }
  .credit-band {
    position: absolute; left: 72px; top: 248px; width: 178px; height: 38px;
    background: var(--brand-red); color: #fff; font-size: 9px; text-align: center;
    padding-top: 7px; line-height: 1.45;
    clip-path: polygon(0 0, 100% 0, 96% 100%, 0 100%);
  }
  .credit-band b { font-weight: 700; }

  .page-title {
    position: absolute; left: 252px; top: 110px;
    font-weight: 100; font-size: 64px; line-height: 1.02; color: #222;
  }
  .page-title .accent { color: var(--brand-red); }

  .body-copy {
    position: absolute; font-size: 9.5px; line-height: 1.55; color: var(--ink);
    text-align: justify; hyphens: auto; overflow: hidden;
  }
  .body-copy--one { left: 90px; top: 300px; width: 180px; height: 330px; }
  .body-copy--two { left: 290px; top: 322px; width: 186px; height: 270px; }

  .signature {
    position: absolute; left: 318px; top: 612px;
    font-family: "Great Vibes", cursive; font-size: 22px; color: #333;
  }
  .folio {
    position: absolute; bottom: 40px; width: 48px; height: 36px;
    background: var(--brand-red); color: #fff; font-size: 14px;
    display: flex; align-items: center; justify-content: center;
  }
  .page--left .folio { left: 0; clip-path: polygon(0 0, 100% 0, 100% 70%, 80% 100%, 0 100%); }
  .page--right .folio { right: 0; clip-path: polygon(20% 0, 100% 0, 100% 100%, 0 100%, 0 30%); }

  .feature-photo {
    position: absolute; left: 44px; top: 62px; width: 430px; height: 598px;
    background: radial-gradient(ellipse at 55% 40%, #b07a5a 0%, var(--photo-warm) 40%, var(--photo-deep) 100%);
  }
  .pull-quote {
    position: absolute; left: 34px; top: 50px; width: 210px; padding: 14px 14px 20px 16px;
    background: var(--brand-red); color: #fff; font-weight: 700; font-size: 12.5px; line-height: 1.35;
    clip-path: polygon(0 0, 100% 0, 100% 100%, 6% 100%, 0 88%);
    box-shadow: 0 2px 6px rgba(0,0,0,.2);
  }
  .photo-caption {
    position: absolute; left: 16px; top: 660px; width: 560px;
    transform-origin: left top; transform: rotate(-90deg);
    font-size: 8.5px; line-height: 1.4; color: var(--ink);
  }
  .photo-caption b { color: var(--brand-red); }
</style>
</head>
<body>
  <main class="spread">
    <section class="page page--left">
      <p class="running-head">OWD | April 2014</p>
      <p class="side-title">Orient Wager Digest</p>

      <div class="editor-portrait" role="img" aria-label="Portrait photograph of the editor"></div>
      <p class="credit-band"><b>Text:</b> Name, <b>Editor:</b> Name<br><b>Photograph:</b> Name</p>

      <h1 class="page-title">Editor<span class="accent">'s</span><br>Letter</h1>

      <p class="body-copy body-copy--one">Livamus imperdiet dui a leo pretium, et rutrum dui consectetur. Integer vulputate porta volutpat. Suspendisse odio metus, dictum eu metus nec, sagittis hendrerit eros. Suspendisse nunc libero, accumsan sit amet ultricies ut, egestas vitae sem. Morbi fringilla porta cursus. Mauris scelerisque, metus lobortis fringilla congue, dolor erat viverra felis, sit amet accumsan lacus nisi id orci. Nunc ut adipiscing erat, egestas tempor quam. Nam eu mattis libero, a malesuada dolor. Vivamus fermentum eget ipsum nec varius. Curabitur eu nulla erat. Donec egestas iaculis tortor, id facilisis mi iaculis eget. Aenean adipiscing purus ac adipiscing rutrum. Suspendisse potenti. Nam elit est, fermentum ut felis eget, gravida accumsan erat.</p>

      <p class="body-copy body-copy--two">Accumsan sit amet ultricies ut, egestas vitae sem. Morbi fringilla porta cursus. Mauris scelerisque, metus lobortis fringilla congue, dolor erat viverra felis, sit amet accumsan lacus nisi id orci. Nam nec suscipit justo. Nunc ut adipiscing erat, egestas tempor quam. Vivamus fermentum eget ipsum nec varius. Nulla facilisi. Morbi dictum urna eget nisi bibendum lacinia. Praesent id arcu enim. Fusce vel posuere eros. Morbi auctor gravida ipsum, ut sagittis erat malesuada non. Donec egestas iaculis tortor, id facilisis mi iaculis eget. Aliquam tincidunt vel enim quis posuere.</p>

      <p class="signature">Your Signature</p>
      <p class="folio">4</p>
    </section>

    <section class="page page--right">
      <p class="running-head">OWD | April 2014</p>
      <span class="running-head-rule"></span>
      <p class="side-title">Orient Wager Digest</p>

      <div class="feature-photo" role="img" aria-label="Photograph of a smiling woman at a casino table pulling in a stack of chips"></div>
      <p class="pull-quote">Nam dapibus enim id condimentum accumsan. Sed sit amet tempor nisi. Proin mollis orci quis erat commodo interdum pharetra.</p>

      <p class="photo-caption"><b>On photo:</b> Accumsan sit amet ultricies ut, egestas vitae sem. Morbi fringilla porta cursus. Mauris scelerisque, metus lobortis fringilla congue, dolor erat viverra felis, sit amet accumsan.</p>

      <p class="folio">5</p>
    </section>
  </main>
</body>
</html>
```